KerrLow Farm

Need a nice simple clean double sided business card that has our logo and info on:
Kerr Low Farm
Martin & Felicity Kerr Low
kerrlowfarm@mailbarn.example
Martin: 1-780-555-0148
Felicity: 1-780-555-0193
Instagram @ kerrlow_farm

Contact Information for Business Card

Martin & Felicity Kerr Low kerrlowfarm@mailbarn.example Martin: 1-780-555-0148 Felicity: 1-780-555-0193

```html
<!DOCTYPE html>
<html lang="en">
<head>
<meta charset="UTF-8">
<title>Kerr Low Farm — Business Card</title>
<link rel="stylesheet" href="https://fonts.googleapis.com/css2?family=Tinos&family=Poppins:wght@400&family=Montserrat:wght@400&display=swap">
<style>
  :root {
    --page-bg: #e9ebe6;
    --farm-green: #67a33f;
    --farm-green-soft: rgba(255,255,255,0.14);
    --wheat-gold: #f0a533;
    --ink: #2b2b2b;
    --card-white: #ffffff;
  }
  * { margin: 0; padding: 0; box-sizing: border-box; }
  html, body { width: 1200px; height: 900px; overflow: hidden; }
  body {
    background: var(--page-bg);
    display: flex;
    flex-direction: column;
    align-items: center;
    justify-content: center;
    gap: 40px;
  }
  .card {
    position: relative;
    width: 700px;
    height: 400px;
    border-radius: 26px;
    overflow: hidden;
    box-shadow: 0 6px 18px rgba(0,0,0,0.18);
  }

  /* Front */
  .card-front { background: var(--farm-green); }
  .front-decoration {
    position: absolute;
    top: 0; right: 0;
    width: 330px; height: 400px;
    background: radial-gradient(ellipse at 65% 35%, var(--farm-green-soft), rgba(255,255,255,0) 70%);
  }
  .front-brand {
    position: absolute;
    left: 0; right: 0; top: 112px;
    display: flex; flex-direction: column; align-items: center;
    color: var(--card-white);
  }
  .brand-circle {
    width: 110px; height: 110px;
    border-radius: 50%;
    border: 4px solid currentColor;
    margin-bottom: 14px;
  }
  .brand-name {
    font-family: "Tinos", serif;
    font-size: 40px;
    letter-spacing: 1px;
    line-height: 1;
  }
  .brand-tagline {
    font-family: "Montserrat", sans-serif;
    font-size: 15px;
    letter-spacing: 9px;
    margin-top: 6px;
  }

  /* Back */
  .card-back { background: var(--card-white); }
  .back-band { position: absolute; inset: 0; }
  .back-brand {
    position: absolute;
    left: 40px; top: 70px;
    width: 300px;
    display: flex; flex-direction: column; align-items: center;
  }
  .back-brand .brand-circle {
    border-color: var(--farm-green);
    background: var(--card-white);
    width: 120px; height: 120px;
    margin-bottom: 10px;
  }
  .back-brand .brand-name { color: var(--farm-green); font-size: 36px; }
  .back-brand .brand-tagline { color: var(--wheat-gold); font-size: 13px; letter-spacing: 8px; }

  .owners-name {
    position: absolute;
    left: 360px; top: 92px;
    font-family: "Tinos", serif;
    font-size: 19px;
    letter-spacing: 1px;
    color: var(--card-white);
    text-transform: uppercase;
  }
  .contact-list {
    position: absolute;
    left: 360px; top: 140px;
    list-style: none;
    font-family: "Poppins", sans-serif;
    font-size: 17px;
    color: var(--ink);
  }
  .contact-item {
    display: flex; align-items: center; gap: 12px;
    height: 34px;
  }
  .contact-icon {
    width: 22px; height: 22px;
    border-radius: 50%;
    background: var(--farm-green);
    display: flex; align-items: center; justify-content: center;
    flex-shrink: 0;
  }
  .contact-icon svg { width: 12px; height: 12px; }
</style>
</head>
<body>

  <section class="card card-front" aria-label="Business card front">
    <div class="front-decoration" role="img" aria-label="Faint wheat stalk decoration"></div>
    <div class="front-brand">
      <div class="brand-circle"></div>
      <div class="brand-name">KERR LOW FARM</div>
      <div class="brand-tagline">STONE MILLED FLOUR</div>
    </div>
  </section>

  <section class="card card-back" aria-label="Business card back">
    <svg class="back-band" viewBox="0 0 700 400" aria-hidden="true">
      <polygon points="0,150 120,150 120,176 0,176" fill="#67a33f"/>
      <polygon points="260,84 700,84 700,116 260,116" fill="#67a33f"/>
      <polygon points="120,150 260,84 260,116 120,176" fill="#67a33f"/>
    </svg>

    <div class="back-brand">
      <div class="brand-circle"></div>
      <div class="brand-name">KERR LOW FARM</div>
      <div class="brand-tagline">STONE MILLED FLOUR</div>
    </div>

    <div class="owners-name">Martin &amp; Felicity Kerr Low</div>

    <ul class="contact-list">
      <li class="contact-item">
        <span class="contact-icon"><svg viewBox="0 0 24 24"><path fill="#fff" d="M6.6 10.8a15 15 0 0 0 6.6 6.6l2.2-2.2c.3-.3.7-.4 1-.2 1.1.4 2.3.6 3.6.6.6 0 1 .4 1 1V20c0 .6-.4 1-1 1A17 17 0 0 1 3 4c0-.6.4-1 1-1h3.5c.6 0 1 .4 1 1 0 1.3.2 2.5.6 3.6.1.3 0 .7-.2 1z"/></svg></span>
        Martin: 1-780-555-0148
      </li>
      <li class="contact-item">
        <span class="contact-icon"><svg viewBox="0 0 24 24"><path fill="#fff" d="M6.6 10.8a15 15 0 0 0 6.6 6.6l2.2-2.2c.3-.3.7-.4 1-.2 1.1.4 2.3.6 3.6.6.6 0 1 .4 1 1V20c0 .6-.4 1-1 1A17 17 0 0 1 3 4c0-.6.4-1 1-1h3.5c.6 0 1 .4 1 1 0 1.3.2 2.5.6 3.6.1.3 0 .7-.2 1z"/></svg></span>
        Felicity: 1-780-555-0193
      </li>
      <li class="contact-item">
        <span class="contact-icon"><svg viewBox="0 0 24 24"><rect x="2" y="5" width="20" height="14" rx="2" fill="#fff"/><path d="M2 6l10 7 10-7" stroke="#67a33f" stroke-width="2" fill="none"/></svg></span>
        kerrlowfarm@mailbarn.example
      </li>
      <li class="contact-item">
        <span class="contact-icon"></span>
        kerrlow_farm
      </li>
    </ul>
  </section>

</body>
</html>
```